New Corporate Email footer (business card design) for 40th Anniversary for Timber Traders

We are traders in sustainable timber worldwide, specialising in tropical hardwoods.
We need to keep our current company logo, but update our email footer with a business card like design which marks the company's 40th Anniversary. 1981-2021. We would need:
Company Logo, Name and Address, website
Sender's: Name, Tel no, fax no, email address
We would need this in a format which we could update ourselves re names/phone numbers if any change.

Target Market(s)

Customers, suppliers, service providers

Contact Information for Business Card

Maria Penhale
Tel: +44 (0) 208 497 3316
Fax: +44 (0) 208 497 2284
Email: maria@rwltimber.example.co.uk
Web: www.rwltimber.example.co.uk

RWL Timber Ltd. 17 Marlow Court, Ashby Crescent, Sanderstead, Surrey KT7 4PZ, UNITED KINGDOM

IMPORTANT NOTICE - This message contains confidential information for the intended addressee only. Any views expressed are those of the sender not RWL Timber Ltd unless otherwise stated. If you receive this message [and any attachment(s)] in error you must not store, copy, disclose or otherwise use any part of it and should advise the sender immediately on 020 8497 5162. Internet communications are not guaranteed secure or virus free. RWL reserves the right to monitor all e-mail communications and does not accept responsibility for any loss or damage resulting from access of this e-mail or any file(s) attached.

Font styles to use
Sans Serif
Other font styles liked:
• not actually sure

Requirements
Must have
• mention of company's 40th Anniversary 1981-2021, which is the whole point of the design
Nice to have
• Our company colour is British Racing Green, but any green theme may be good
Maybe a tree design but allowing the company logo to stand out.

```html
<!DOCTYPE html>
<html lang="en">
<head>
<meta charset="utf-8">
<title>RWL Timber – 40th Anniversary Business Card</title>
<link rel="stylesheet" href="https://fonts.googleapis.com/css2?family=Montserrat:wght@600;800&family=Arimo:wght@400&display=swap">
<style>
  :root {
    --backdrop: #2a2a2b;
    --card: #1e1c1d;
    --card-edge: #2b2829;
    --white: #ffffff;
    --rule: #cfcfcf;
    --gold-light: #f6cf6a;
    --gold: #d9a032;
    --gold-dark: #a8721c;
  }
  html, body {
    margin: 0;
    padding: 0;
    width: 1200px;
    height: 900px;
    overflow: hidden;
    background: var(--backdrop);
  }
  .canvas {
    position: relative;
    width: 1200px;
    height: 900px;
  }
  .card {
    position: absolute;
    width: 620px;
    height: 354px;
    border-radius: 22px;
    background: linear-gradient(135deg, var(--card-edge) 0%, var(--card) 55%, #161415 100%);
    overflow: hidden;
    box-shadow: 0 12px 30px rgba(0,0,0,.45);
  }
  .card--front { left: 70px; top: 70px; }
  .card--back  { left: 510px; top: 476px; }

  .brand {
    position: absolute;
    display: flex;
    align-items: center;
    gap: 12px;
    font-family: "Montserrat", sans-serif;
    font-weight: 800;
    color: var(--white);
    letter-spacing: 1px;
    line-height: 1;
  }
  .brand__dot {
    border-radius: 50%;
    background: var(--white);
  }
  .card--front .brand { left: 50%; top: 50%; transform: translate(-50%, -50%); font-size: 64px; }
  .card--front .brand__dot { width: 56px; height: 56px; }
  .card--back .brand { left: 40px; top: 176px; font-size: 46px; }
  .card--back .brand__dot { width: 40px; height: 40px; }

  .holder-name {
    position: absolute;
    right: 44px;
    top: 34px;
    font-family: "Montserrat", sans-serif;
    font-weight: 800;
    font-size: 21px;
    letter-spacing: 1.5px;
    text-transform: uppercase;
    background: linear-gradient(180deg, var(--gold-light), var(--gold) 60%, var(--gold-dark));
    -webkit-background-clip: text;
    background-clip: text;
    color: transparent;
  }
  .rule {
    position: absolute;
    height: 1px;
    background: var(--rule);
  }
  .rule--top { left: 250px; right: 34px; top: 150px; }
  .rule--contacts { left: 40px; width: 250px; top: 248px; }

  .contacts {
    position: absolute;
    left: 40px;
    top: 256px;
    margin: 0;
    padding: 0;
    list-style: none;
    font-family: "Arimo", sans-serif;
    font-size: 14px;
    line-height: 20px;
    color: var(--white);
  }
  .contacts li { display: flex; align-items: center; gap: 9px; }
  .contacts__icon {
    width: 15px;
    height: 15px;
    border-radius: 3px;
    background: linear-gradient(180deg, var(--gold-light), var(--gold-dark));
    display: inline-flex;
    align-items: center;
    justify-content: center;
  }
  .contacts__icon svg { width: 11px; height: 11px; }

  .anniversary-seal {
    position: absolute;
    right: 34px;
    top: 172px;
    width: 118px;
    height: 118px;
  }
  .anniversary-seal__ring {
    position: absolute;
    left: 9px;
    top: 0;
    width: 96px;
    height: 96px;
    box-sizing: border-box;
    border-radius: 50%;
    border: 3px solid var(--gold);
    box-shadow: inset 0 0 0 4px var(--card), inset 0 0 0 5px var(--gold-dark);
    display: flex;
    flex-direction: column;
    align-items: center;
    font-family: "Montserrat", sans-serif;
    color: var(--gold);
  }
  .anniversary-seal__years {
    margin-top: 12px;
    font-weight: 600;
    font-size: 9px;
    letter-spacing: .5px;
  }
  .anniversary-seal__number {
    margin-top: 2px;
    font-weight: 800;
    font-size: 38px;
    line-height: 1;
    color: var(--gold-light);
  }
  .anniversary-seal__number sup {
    font-size: 12px;
    vertical-align: top;
    position: relative;
    top: 2px;
  }
  .anniversary-seal__ribbon {
    position: absolute;
    left: 0;
    right: 0;
    top: 72px;
    height: 18px;
    background: linear-gradient(180deg, var(--gold-light), var(--gold) 60%, var(--gold-dark));
    font-family: "Montserrat", sans-serif;
    font-weight: 800;
    font-size: 10px;
    letter-spacing: 1.5px;
    line-height: 18px;
    text-align: center;
    color: var(--card);
  }
  .gold-edge {
    position: absolute;
    left: 0;
    right: 0;
    bottom: 0;
    height: 9px;
    background: linear-gradient(90deg, var(--gold-dark), var(--gold-light) 45%, var(--gold) 70%, var(--gold-dark));
  }
</style>
</head>
<body>
<main class="canvas">

  <section class="card card--front" aria-label="Card front">
    <div class="brand"><span class="brand__dot"></span>RWL</div>
  </section>

  <section class="card card--back" aria-label="Card back">
    <div class="holder-name">Maria Penhale</div>
    <div class="rule rule--top"></div>

    <div class="brand"><span class="brand__dot"></span>RWL</div>

    <div class="anniversary-seal">
      <div class="anniversary-seal__ring">
        <span class="anniversary-seal__years">1981-2021</span>
        <span class="anniversary-seal__number">40<sup>th</sup></span>
      </div>
      <div class="anniversary-seal__ribbon">ANNIVERSARY</div>
    </div>

    <div class="rule rule--contacts"></div>
    <ul class="contacts">
      <li>
        <span class="contacts__icon"><svg viewBox="0 0 12 12"><path d="M3 1.5l1.6 2.2-1 1.1c.6 1.3 1.6 2.3 2.9 2.9l1.1-1 2.2 1.6-.8 1.9C5.5 10 2 6.5 1.8 2.3z" fill="#1e1c1d"/></svg></span>
        +44 (0) 208 497 3316
      </li>
      <li>
        <span class="contacts__icon"><svg viewBox="0 0 12 12"><rect x="3" y="1.5" width="6" height="3" fill="none" stroke="#1e1c1d" stroke-width="1"/><rect x="1.5" y="4.5" width="9" height="5" rx="1" fill="#1e1c1d"/><rect x="3.5" y="7" width="5" height="3.5" fill="#f6cf6a" stroke="#1e1c1d" stroke-width=".8"/></svg></span>
        +44 (0) 208 497 2284
      </li>
      <li>
        <span class="contacts__icon"><svg viewBox="0 0 12 12"><rect x="1.5" y="3" width="9" height="6.5" fill="none" stroke="#1e1c1d" stroke-width="1.1"/><path d="M1.5 3L6 7l4.5-4" fill="none" stroke="#1e1c1d" stroke-width="1.1"/></svg></span>
        maria@rwltimber.example.co.uk
      </li>
      <li>
        <span class="contacts__icon"><svg viewBox="0 0 12 12"><circle cx="6" cy="6" r="4.3" fill="none" stroke="#1e1c1d" stroke-width="1"/><ellipse cx="6" cy="6" rx="1.9" ry="4.3" fill="none" stroke="#1e1c1d" stroke-width=".9"/><path d="M1.7 6h8.6" stroke="#1e1c1d" stroke-width=".9"/></svg></span>
        www.rwltimber.example.co.uk
      </li>
    </ul>

    <div class="gold-edge"></div>
  </section>

</main>
</body>
</html>
```